Tarvel Ridge LLC

Need Professional Business cards for New Investment Fund

Target Market(s)

High Quality investors

Industry/Entity Type

Financial

Contact Information for Business Card

Phone Number +1 555 284 6193
Name Pavel Orlinsky
Title Fund Manager
email po@FundTarvel.example
Website www.FundTarvel.example

Colors

Designer to choose colors to be used in the design.

Requirements
Must have
• Must have our Logo and all of the above. Must be made so lettering and loge can be raised

```html
<!DOCTYPE html>
<html lang="en">
<head>
<meta charset="utf-8">
<title>Tarvel Ridge LLC — Business Card</title>
<link rel="stylesheet" href="https://fonts.googleapis.com/css2?family=Jost:wght@400;500&display=swap">
<style>
  :root {
    --page: #f4f4f6;
    --card: #ffffff;
    --green: #58b94c;
    --forest: #414d42;
    --mist: #cfe5c2;
    --ink: #111111;
    --grey: #8a9098;
  }
  * { box-sizing: border-box; margin: 0; padding: 0; }
  html, body {
    width: 1200px; height: 1200px; overflow: hidden;
    background: var(--page);
    font-family: "Jost", "Futura", sans-serif;
  }
  .card {
    position: absolute; left: 206px; width: 788px; height: 450px;
  }
  .card--front { top: 112px; background: var(--card); }
  .card--back  { top: 638px; background: var(--green); }

  .brand {
    position: absolute; display: flex; align-items: center; gap: 12px;
    font-weight: 500; white-space: nowrap;
  }
  .brand__mark { width: 22px; height: 22px; flex: none; }
  .card--front .brand { left: 118px; top: 198px; font-size: 30px; color: var(--forest); }
  .card--front .brand__mark { background: var(--green); }
  .card--back .brand { left: 50%; top: 50%; transform: translate(-50%, -50%); font-size: 48px; color: var(--mist); gap: 18px; }
  .card--back .brand__mark { width: 34px; height: 34px; background: var(--forest); }

  .person { position: absolute; left: 363px; top: 136px; }
  .person__name { font-size: 30px; font-weight: 400; color: var(--ink); line-height: 1; letter-spacing: 0.3px; }
  .person__title { margin-top: 6px; font-size: 21px; color: var(--grey); letter-spacing: 0.4px; }

  .contacts { position: absolute; left: 357px; top: 240px; list-style: none; }
  .contacts__item {
    display: flex; align-items: center; height: 41px;
    font-size: 21px; letter-spacing: 1.6px; color: var(--grey);
  }
  .contacts__item--web { color: var(--green); }
  .contacts__icon { width: 24px; height: 24px; margin-right: 14px; flex: none; }

  .stripe { position: absolute; left: 0; bottom: 0; width: 100%; height: 22px; display: flex; }
  .stripe__green { flex: 1; background: var(--green); }
  .stripe__forest { flex: 1; background: var(--forest); }
</style>
</head>
<body>
  <section class="card card--front">
    <div class="brand"><span class="brand__mark"></span>Tarvel Ridge</div>

    <div class="person">
      <h1 class="person__name">Pavel Orlinsky</h1>
      <p class="person__title">Title Fund Manager</p>
    </div>

    <ul class="contacts">
      <li class="contacts__item">
        <svg class="contacts__icon" viewBox="0 0 24 24" aria-hidden="true">
          <path d="M9 3 L12 3 L12 8 L10 9 Q9 12 10 15 L12 16 L12 21 L9 21 Q6 17 6 12 Q6 7 9 3 Z" fill="var(--green)"/>
        </svg>
        +1 555 284 6193
      </li>
      <li class="contacts__item">
        <svg class="contacts__icon" viewBox="0 0 24 24" aria-hidden="true">
          <rect x="1" y="5" width="22" height="14" fill="var(--green)"/>
          <path d="M1 5 L12 13 L23 5 M1 19 L9 11 M23 19 L15 11" stroke="#fff" stroke-width="1.6" fill="none"/>
        </svg>
        po@FundTarvel.example
      </li>
      <li class="contacts__item contacts__item--web">
        <svg class="contacts__icon" viewBox="0 0 24 24" aria-hidden="true">
          <circle cx="12" cy="12" r="11" fill="var(--green)"/>
          <path d="M6 6 Q10 7 9 11 Q12 13 10 17 M15 4 Q14 8 18 9 Q20 13 17 17" stroke="#fff" stroke-width="1.8" fill="none"/>
        </svg>
        www.FundTarvel.example
      </li>
    </ul>

    <div class="stripe"><span class="stripe__green"></span><span class="stripe__forest"></span></div>
  </section>

  <section class="card card--back">
    <div class="brand"><span class="brand__mark"></span>Tarvel Ridge</div>
  </section>
</body>
</html>
```